Bright Quest Appeal needs a brochure

I need an A4 - Two sided brochure design.
It's for a maths challenge fundraiser for primary schools throughout Australia.
It needs to be bright and fun with the pictures / files supplied,
Please use as many pics as you can, more the better...
Also keep Logos as transparent
See our website for an idea of what we do pls. thebrightquest.example
Pls make it FUN ....NOT corporate..
so curves and colours rather than straight lines
The only headings that need to be ALL capitals is "FREE TO JOIN" & "FUNDRAISER" Other titles not all capitals pls
Please note: when putting in the pics of the games, pls put in order from game1-7 as they go in order of the school grade levels (Preschool to Grade 6). showing teachers how they become more difficult...in that order.
This brochure will be sent to schools.
Schools have admin open letters, we get about 2 - 3 seconds for admin to decide to keep or bin the brochure, so they need to see it's a fundraiser and "free to join" in those seconds.
cheers
- fun style maybe marker felt or comic sans but you choose any other you think works to make it fun

```html
<!DOCTYPE html>
<html lang="en">
<head>
<meta charset="utf-8">
<title>Bright Quest Appeal – Maths Challenge Fundraiser</title>
<link href="https://fonts.googleapis.com/css2?family=Cabin+Sketch:wght@700&family=Kalam:wght@700&family=Source+Sans+3:wght@400;700&display=swap" rel="stylesheet">
<style>
  :root {
    --teal: #a8d8da;
    --blue: #3f7599;
    --red: #e0122a;
    --text: #4a4a4a;
    --paper: #ffffff;
    --gold-light: #f3d37a;
    --gold-dark: #c39a36;
  }
  * { margin: 0; padding: 0; box-sizing: border-box; }
  html, body { width: 848px; height: 1200px; overflow: hidden; background: var(--paper); }
  .brochure { position: relative; width: 848px; height: 1200px; background: var(--paper); font-family: "Source Sans 3", sans-serif; color: var(--text); }

  .hero-frame { position: absolute; left: 63px; top: 0; width: 785px; height: 302px; background: var(--teal); border-bottom-left-radius: 150px; }
  .hero-photo { position: absolute; left: 73px; top: 0; width: 775px; height: 293px; border-bottom-left-radius: 140px;
    background: linear-gradient(100deg, #161616 0%, #1d1d1d 55%, #3a3330 72%, #b89a88 82%, #2a2a2a 100%); }
  .brand { position: absolute; left: 150px; top: 128px; display: flex; align-items: center; gap: 10px; }
  .brand-dot { width: 26px; height: 26px; border-radius: 50%; background: var(--red); }
  .brand-name { font-family: "Kalam", cursive; font-weight: 700; font-size: 24px; color: var(--red); }

  .kicker { position: absolute; top: 318px; left: 0; width: 848px; text-align: center; font-family: "Kalam", cursive; font-weight: 700; font-size: 52px; color: var(--blue); line-height: 1.1; }
  .headline { position: absolute; top: 370px; left: 0; width: 848px; text-align: center; font-family: "Cabin Sketch", cursive; font-weight: 700; font-size: 126px; color: var(--red); line-height: 1; white-space: nowrap; }
  .tagline { position: absolute; top: 482px; left: 0; width: 848px; text-align: center; font-family: "Kalam", cursive; font-weight: 700; font-size: 23px; color: var(--blue); white-space: nowrap; }

  .section-title { font-family: "Kalam", cursive; font-weight: 700; color: var(--red); line-height: 1.15; text-align: center; white-space: nowrap; }
  .copy p { font-size: 17px; line-height: 24.3px; text-align: center; margin-bottom: 8px; white-space: nowrap; }
  .copy .strong { font-weight: 700; }

  .challenge { position: absolute; left: 46px; top: 536px; width: 400px; }
  .challenge .section-title { font-size: 29px; letter-spacing: -0.3px; margin-bottom: 20px; }

  .photo-backing { position: absolute; background: var(--teal); }
  .photo { position: absolute; }
  .backing-high-five { left: 478px; top: 552px; width: 309px; height: 263px; border-radius: 34px 0 34px 0; }
  .photo-high-five { left: 467px; top: 542px; width: 310px; height: 263px; border-radius: 34px 0 34px 0;
    background: linear-gradient(160deg, #cfe6f3 0%, #e8eef2 45%, #2e8fb0 80%, #d8c4ac 100%); }
  .certificate { position: absolute; left: 444px; top: 597px; width: 164px; height: 229px; transform: rotate(-2deg);
    background: linear-gradient(150deg, var(--gold-light), var(--gold-dark)); box-shadow: 2px 3px 6px rgba(0,0,0,.25); }

  .backing-class { left: 69px; top: 840px; width: 361px; height: 315px; border-radius: 0 0 0 34px; }
  .photo-class { left: 59px; top: 828px; width: 359px; height: 314px; border-radius: 34px 0 34px 0;
    background: linear-gradient(170deg, #9ec0d6 0%, #e9b9a8 40%, #d3446f 60%, #b78a66 100%); }

  .join { position: absolute; left: 431px; top: 845px; width: 380px; }
  .join .section-title { font-size: 31px; margin-bottom: 14px; }
</style>
</head>
<body>
<main class="brochure">
  <div class="hero-frame"></div>
  <div class="hero-photo" role="img" aria-label="Photo of a smiling girl raising both arms in front of a chalkboard covered in sums"></div>
  <div class="brand">
    <span class="brand-dot"></span>
    <span class="brand-name">thebrightquest.example</span>
  </div>

  <h2 class="kicker">Maths Challenge</h2>
  <h1 class="headline">FUNDRAISER</h1>
  <p class="tagline">"A great fundraiser helping primary school students with maths!"</p>

  <section class="challenge copy">
    <h3 class="section-title">Students love a challenge!</h3>
    <p>Students are challenged to solve educational<br>maths games on The Bright Quest website.</p>
    <p class="strong">It’s lots of fun and helps students with maths!</p>
    <p>A maths challenge designed to build<br>confidence in mathematics for Australian<br>Primary School students. Once students have<br>completed their maths challenge, they may<br>download a certificate of congratulations.</p>
  </section>

  <div class="photo-backing backing-high-five"></div>
  <div class="photo photo-high-five" role="img" aria-label="Photo of a boy giving a high five beside a tablet at his desk"></div>
  <div class="certificate" role="img" aria-label="Gold certificate of congratulations awarded for completing the challenge"></div>

  <div class="photo-backing backing-class"></div>
  <div class="photo photo-class" role="img" aria-label="Photo of a class of primary students sitting on the floor with hands raised"></div>

  <section class="join copy">
    <h3 class="section-title">Free to Join!<br>Effortless to run!</h3>
    <p>It’s all set-up online and ready to go. No<br>spending time or effort planning activities<br>or fundraiser days.</p>
    <p>The Bright Quest website is fully safe<br>and secure with no information sharing,<br>no links to other sites and no popup<br>advertising. Plus, all Bright Quest<br>games are aligned with the Australian<br>Mathematics Curriculum.</p>
  </section>
</main>
</body>
</html>
```